NOTE: I PROVIDED THE INCORRECT LOGO AND ONLY A HANDFUL OF PEOPLE NOTICED THAT IT WAS NOT THE ONE I DESCRIBED. THE LOGO I HAVE NOW ATTACHED MATCHES MY WEBSITE AND THE COLORS ON THE WEBSITE SHOULD BE USED FOR THE CARD.

PLEASE READ THE BUSINESS CARD DETAILS AND PROJECT MUST HAVES CAREFULLY.

I am looking for a business card that is powerful, a bit edgy, and although I work in the corporate world, not too formal. I would like to see designs that use the colors on my website www.brightmoorlane.com. I don't want the card to look washed out so please use shades of those colors that make them "pop". The "vibe" of the card needs to show substance and confidence while also reflecting that we're not your usual consultants.

The focus of my work is turning "people problems" into profits. Those problems could be poor service, an unstable workforce, untrained leaders, or managing change. We are an aggressive, results-focused team of performance improvement professionals who refuse to believe "things can't be done". For us, failure is not an option. Our logo reflects a target from the view of the site on a gun.

In addition to the contact information provided on the sample business card (do not include "turning people problems into profits"), I would like to include this statement (probably on the back):
I equip results-oriented business leaders to turn their people problems into profits in six months or less.

PLEASE NOTE THAT MY WEBSITE IS UNDER REVISION TO TONE DOWN THE MILITARY THEME, ALTHOUGH THE WARRIOR ENERGY AND FOCUS ON RESULTS REMAINS.

Target Market(s)

My clients are Mid and senior-level managers. I don't target any particular industry.

Industry/Entity Type

Consulting

Contact Information for Business Card

In addition to the contact information provided on the sample business card (DO NOT INCLUDE "turning people problems into profits"), I would like to include this statement (probably on the back):

I don't care whether the card is landscape or portrait view.

Font styles to use
Sans Serif

Requirements
Must have
• 1. be easy to read, no 6-8 point fonts!
• 2. a "vibe" that captures the eye without being too chaotic or busy
• 3. bold color, not washed out or boring - a good blend with the colors currently on my website (black, red, white, army green) but you don't need to use all of them.
• 4. all the contact information I have provided
• 5. a good blend with the colors currently on my website
• 6. Must have this quote on the back of the card: I equip results-oriented business leaders to turn their people problems into profits in six months or less.
Nice to have
• In looking at the sample images I provided for ideas, you can see that I like the way a card carries over from one side to the next.
• It would be great to find some aspect/quality/feature that I haven't seen before
Should not have
• 1. NO use of ALL CAPS
• 2. fonts that I would have to seek out and purchase (you should provide files for font if using something not standard)

```html
<!DOCTYPE html>
<html lang="en">
<head>
<meta charset="utf-8">
<title>Brightmoor Lane – Business Card</title>
<link href="https://fonts.googleapis.com/css2?family=Work+Sans:wght@400;500;700;800&display=swap" rel="stylesheet">
<style>
  :root {
    --page: #2a2a2a;
    --card-dark: #1c1c1c;
    --card-light: #ffffff;
    --accent-red: #e8372c;
    --army-green: #383d2e;
    --text-light: #f2f2f2;
  }
  * { box-sizing: border-box; margin: 0; padding: 0; }
  html, body {
    width: 1200px; height: 930px; overflow: hidden;
    background: var(--page);
    font-family: "Work Sans", Arial, sans-serif;
  }
  .canvas { position: relative; width: 1200px; height: 930px; }

  .card {
    position: absolute;
    width: 760px; height: 434px;
    border-radius: 22px;
    overflow: hidden;
    background: var(--card-dark);
    box-shadow: 0 10px 30px rgba(0,0,0,.45);
  }
  .card--back { left: 70px; top: 30px; }
  .card--front { left: 370px; top: 466px; }

  /* Brand name */
  .brand {
    display: flex; align-items: center; gap: 12px;
    font-weight: 800; letter-spacing: -0.5px; line-height: 1;
    white-space: nowrap;
  }
  .brand__dot { width: 20px; height: 20px; border-radius: 50%; background: var(--accent-red); flex: none; }

  /* Back */
  .card--back .brand {
    position: absolute; left: 0; right: 0; top: 140px;
    justify-content: center;
    font-size: 50px; color: var(--text-light);
  }
  .mission {
    position: absolute; left: 110px; right: 110px; top: 262px;
    color: var(--text-light); font-size: 18px; line-height: 1.45; text-align: center;
  }

  /* Front */
  .front-sweep { position: absolute; inset: 0; }
  .card--front .brand {
    position: absolute; left: 330px; top: 100px;
    font-size: 38px; color: var(--army-green);
  }
  .contact { position: absolute; left: 48px; top: 212px; color: var(--text-light); }
  .contact__name { color: var(--accent-red); font-size: 28px; font-weight: 500; letter-spacing: .5px; }
  .contact__title { font-size: 17px; font-weight: 500; margin-top: 2px; }
  .contact__address { font-size: 16px; line-height: 1.3; margin-top: 12px; }
  .contact__list { list-style: none; margin-top: 10px; font-size: 16px; }
  .contact__list li { display: flex; align-items: center; gap: 12px; line-height: 1.4; }
  .contact__list svg { width: 14px; height: 14px; flex: none; }
  .contact__web-highlight { color: var(--accent-red); }
</style>
</head>
<body>
<main class="canvas">

  <section class="card card--back" aria-label="Card back">
    <div class="brand"><span class="brand__dot"></span><span class="brand__name">Brightmoor Lane</span></div>
    <p class="mission">I equip results-oriented business leaders to turn their people problems into profits in six months or less.</p>
  </section>

  <section class="card card--front" aria-label="Card front">
    <svg class="front-sweep" viewBox="0 0 760 434" width="760" height="434" aria-hidden="true">
      <path d="M230 0 C300 190 520 330 760 300 L760 0 Z" fill="var(--card-light)"/>
      <path d="M218 0 C290 200 520 345 760 300" fill="none" stroke="var(--accent-red)" stroke-width="9"/>
      <path d="M228 0 C300 192 520 333 760 301" fill="none" stroke="var(--card-light)" stroke-width="4"/>
    </svg>

    <div class="brand"><span class="brand__dot"></span><span class="brand__name">Brightmoor Lane</span></div>

    <div class="contact">
      <p class="contact__name">DANA WHITFIELD</p>
      <p class="contact__title">Chief Performance Strategist</p>
      <p class="contact__address">1418 Harlow Avenue #210<br>Ferndale, MI 48220</p>
      <ul class="contact__list">
        <li><svg viewBox="0 0 16 16"><path d="M3 1l3 3-2 2c1 2 3 4 5 5l2-2 3 3-2 3C7 15 1 9 1 3z" fill="var(--accent-red)"/></svg><span>248-555-0147</span></li>
        <li><svg viewBox="0 0 16 16"><rect x="4" y="1" width="8" height="14" rx="2" fill="none" stroke="var(--accent-red)" stroke-width="1.6"/></svg><span>248-555-0193</span></li>
        <li><svg viewBox="0 0 16 16"><rect x="1" y="3" width="14" height="10" rx="1" fill="none" stroke="var(--accent-red)" stroke-width="1.6"/><path d="M1 4l7 5 7-5" fill="none" stroke="var(--accent-red)" stroke-width="1.6"/></svg><span>danaw@brightmoorlane.com</span></li>
        <li><svg viewBox="0 0 16 16"><circle cx="8" cy="8" r="6.5" fill="none" stroke="var(--accent-red)" stroke-width="1.6"/><path d="M1.5 8h13M8 1.5c-3 3-3 10 0 13M8 1.5c3 3 3 10 0 13" fill="none" stroke="var(--accent-red)" stroke-width="1.2"/></svg><span>www.<span class="contact__web-highlight">brightmoorlane</span>.com</span></li>
      </ul>
    </div>
  </section>

</main>
</body>
</html>
```